Spanish winery needs a label design for a red, white and rosé wine.

We need a front and back label for our representee Garrido Velasquez SL, a wine producer in the Spanish region of Extremadura.

Trademark: Sereneto. Sereneto means balanced in English. The message is that the wine show the equilibrium of the blends specially produced for this project, it is balanced in the mounth and nose and it,s a good balance between quality and price.

Target: Wine targets entry level market retail sector in Europe so it cannot be too fancy.

Style: Spanish wines are better seen with a classic touch in the design although a bit of modernity is required.

Number of labels: 3 front and 3 back labels required although you can use the same design and just change the colors. Bottle is a bordeaux style 30 mm high with an screw cup closure, green for the red and transparent for the white and rosé.

Labels size: front max 90 (wide)x130 (high)mm. Back max 85 (w)x85(h)mm.

Information to include in the front label: Trademark, type of wine (red, white or rosé), two short lines of text with tasting notes (see texts on doc file), capacity 75cl, ABV:11º vol. Bottled by Garrido Velásquez SL C/Almadena 27. 06480 Villar del Caminal (Badajoz). Spain.

Information to be included in the back label:trademark, type of wine, tasting notes (see texts on doc file), Capacity 75cl, Filling control mark: E, Barcode, Allergy advise, Contains sulfites advise, Pregnant women advise.

Paper: Shiny or matt paper with possibility of foil printing. No embossed effects.

Please see attached Val de Piedra label as a reference of the necessary information to be contained by labels.
Updates

Reason: We would like to give a bit more of time to those that have accepted and have not yet submitted a design.

Target Market(s)

Entry level european consumers

Industry/Entity Type

Retail

Requirements
Nice to have
• Maybe a clasical scale, old coins (balanced in cost).... Balance is the route to follow.

```html
<!DOCTYPE html>
<html lang="en">
<head>
<meta charset="utf-8">
<title>Sereneto wine labels</title>
<link rel="stylesheet" href="https://fonts.googleapis.com/css2?family=Crimson+Text:wght@400;600&display=swap">
<style>
  :root {
    --page: #ffffff;
    --band-grey: #5c5c5c;
    --band-wine: #1e0000;
    --charcoal: #2b2a29;
    --ink-light: #f2f2f2;
    --box-line: #8a8a8a;
  }
  * { margin: 0; padding: 0; box-sizing: border-box; }
  html, body { width: 1200px; height: 1000px; overflow: hidden; background: var(--page); }
  body { position: relative; font-family: "Crimson Text", Georgia, serif; color: var(--ink-light); }

  .label { position: absolute; }
  .front-label { left: 136px; top: 204px; width: 449px; height: 574px; }
  .back-label { left: 614px; top: 235px; width: 424px; height: 423px; background: var(--charcoal); }

  .origin { position: absolute; top: 8px; font-size: 20px; letter-spacing: 0.3px; }
  .origin-left { left: 8px; }
  .origin-right { right: 8px; }
  .back-label .origin { top: 8px; font-size: 17px; }

  .brand-band { position: absolute; left: 0; top: 0; width: 100%; height: 231px; background: var(--band-grey); }
  .brand-name { position: absolute; left: 0; width: 100%; text-align: center; font-weight: 400; text-transform: uppercase; }
  .front-label .brand-name { top: 130px; font-size: 50px; letter-spacing: 4px; }
  .back-label .brand-name { top: 92px; font-size: 32px; letter-spacing: 3px; }

  .tasting-band { position: absolute; left: 0; top: 231px; width: 100%; height: 194px; background: var(--band-wine); text-align: center; }
  .tasting-note { margin-top: 32px; font-size: 24px; line-height: 32px; }
  .wine-type { margin-top: 26px; font-size: 44px; letter-spacing: 3px; line-height: 1; }

  .info-band { position: absolute; left: 0; top: 425px; width: 100%; height: 149px; background: var(--charcoal); }
  .bottler { margin-top: 37px; text-align: center; font-size: 14px; line-height: 18px; }

  .capacity, .abv { position: absolute; bottom: 4px; font-size: 30px; line-height: 1; }
  .capacity { left: 10px; }
  .abv { right: 10px; }
  .estimated-sign { font-size: 42px; }
  .back-label .capacity, .back-label .abv { bottom: 8px; font-size: 19px; }
  .back-label .capacity { left: 11px; }
  .back-label .abv { right: 10px; }

  .back-description { position: absolute; left: 0; top: 166px; width: 100%; text-align: center; font-size: 16px; line-height: 20px; }

  .info-box { position: absolute; top: 268px; width: 173px; height: 108px; border: 1px solid var(--box-line); text-align: center; font-size: 16px; padding-top: 10px; }
  .allergy-box { left: 25px; }
  .barcode-box { left: 224px; }
</style>
</head>
<body>
  <section class="label front-label">
    <div class="brand-band">
      <span class="origin origin-left">PRODUCT</span>
      <span class="origin origin-right">OF SPAIN</span>
      <h1 class="brand-name">Sereneto</h1>
    </div>
    <div class="tasting-band">
      <p class="tasting-note">Seductively soft and smooth red wine<br>displaying delicious fruit flavours.</p>
      <p class="wine-type">VINO TINTO</p>
    </div>
    <div class="info-band">
      <p class="bottler">Bottled by Garrido Velásquez SL C/Almadena 27.<br>06480 Villar del Caminal (Badajoz).<br>Spain.</p>
      <span class="capacity">75cl <span class="estimated-sign">e</span></span>
      <span class="abv">11% vol</span>
    </div>
  </section>

  <section class="label back-label">
    <span class="origin origin-left">PRODUCT</span>
    <span class="origin origin-right">OF SPAIN</span>
    <h2 class="brand-name">Sereneto</h2>
    <p class="back-description">Sereneto tinto is a soft, easy drinking dry red wine, full<br>of delicious ripe fruit flavours.<br>Enjoy it with tapas food or simply on its own.<br>Ready to drink now. Best served at room temperature.</p>
    <div class="info-box allergy-box">Allergy Advice</div>
    <div class="info-box barcode-box">Barcode</div>
    <span class="capacity">75cl e</span>
    <span class="abv">11% vol</span>
  </section>
</body>
</html>
```